依頼詳細
デザインしていただくのはチューブ容器のプリント部分のデザインです。
パッケージに使用できるカラーは2色です。

キーワードとしては「ネガティブなイメージがない。」「肌にやさしい。」「効き目がありそう。」というようなものになり、シンプル・スタイリッシュ・ナチュラルな雰囲気の高級感のあるデザインをお願いします。

■参考デザイン・ブランド

フェルモア http://www.felmore.co.jp/
TRリネ http://www.haldenvik.co.jp/products/rine/dayveil/
記載項目
デザイン範囲:151mm × 縦は未定(別途資料を参考にして下さい。)
チューブ容器のカラーは白。着色不可。
使用可能色数は2色まで。シルクスクリーン印刷になります。
シルク印刷特有のズレ等を考慮したデザインをお願いします。
デザイン範囲は別途添付してあるデータを参考に制作してください。

半分より左側には表面のデザインを、右側には裏面の責任事項が入ります。
表面デザインには「商品名: VELQUETE 」を必ず入れて下さい。
裏面デザインには別途添付データにある「責任事項」(変更不可)を必ず入れて下さい。

全てのデザインを通して、使用可能な最小フォントサイズは6~7ptまでです。(コピー用紙などにプリントアウトして潰れないサイズであれば大丈夫です。)モチーフ・ロゴマーク等の絵柄の有無は問いません。

複雑な絵柄は不可です。
文字と絵柄が重なるのも不可です。
希望イメージ
シンプル 複雑
単色 カラフル
暗い 明るい
日常 高級
遊び心 厳粛
未来的 伝統的
女性的 男性的
希望する色
使用可能色数は2色です。その中で、お任せいたします。
納品ファイル
• イラストレーター形式 (.ai)
補足説明
■ 進め方

弊社の希望するイメージに近い提案を1つ(場合によって複数)選択させて頂きます。
希望に近づけるために、修正要望を個別にさせて頂くこともあります。
コンペ方式のため、修正後に当選されない場合もございますが、どうかご了承ください。

当選者の方には入稿データまで制作をお願いします。
当選後に3~4回程細かい修正や調整をお願いする場合があります。

■ その他/注意点

選択させて頂いたデザインの著作権(財産権)等の扱いはTaskora利用規約に従い、弊社に譲渡をお願いします。フォントや画像素材などを利用する場合は上記利用用途に使用できることを確認し、第三者の知的財産権等に注意して下さい。
デザインに必要なファイルと参考画像をアップしました。
沢山のエントリーありがとうございます。

ナチュラルというキーワードを反映した素敵なデザインが多く、どきどきしながら進捗を見守っております。あと数日となりましたが「ブラック」で高級感のあるパッケージのご提案も見てみたいと思っております。

引き続き沢山のエントリーをお待ちしております。
よろしくお願い致します。
■ 選んだ理由

今回の商品にあったフォントと、発展性のあるデザインということで決定させていただきました。

■ 提案者全員のお礼・コメント

弊社の予想をはるかに超えるタスコラーからのご提案、誠にありがとうございました。多くの良案をいただき、購入対象者の方にアンケートを行い絞り込みをさせていただくという流れをとらせていただくまでの大きなコンペとなりました。またコンペを開催の折には、ご連絡させていただければと思っております。この度は、本当にありがとうございました。

```html
<!DOCTYPE html>
<html lang="ja">
<head>
<meta charset="utf-8">
<title>VELQUETE remover cream – tube print</title>
<link rel="stylesheet" href="https://fonts.googleapis.com/css2?family=Anton&family=Roboto+Condensed:wght@300;400&display=swap">
<style>
  :root {
    --tube-white: #ffffff;
    --page-bg: #f2f2f2;
    --ink-black: #1a1a1a;
    --ink-grey: #4a4a4a;
  }
  html, body {
    margin: 0;
    padding: 0;
    width: 732px;
    height: 1200px;
    overflow: hidden;
    background: var(--page-bg);
  }
  .print-area {
    position: relative;
    width: 732px;
    height: 1200px;
    background: var(--tube-white);
    overflow: hidden;
  }
  .brand-vertical {
    position: absolute;
    top: 60px;
    left: 150px;
    margin: 0;
    writing-mode: vertical-rl;
    text-orientation: sideways;
    font-family: "Anton", "Impact", sans-serif;
    font-weight: 400;
    font-size: 300px;
    line-height: 1;
    letter-spacing: 4px;
    color: var(--ink-black);
    white-space: nowrap;
  }
  .product-label {
    position: absolute;
    left: 470px;
    top: 1010px;
    font-family: "Roboto Condensed", "Arial Narrow", sans-serif;
    color: var(--ink-grey);
    line-height: 1.15;
  }
  .product-label__name {
    display: block;
    font-size: 22px;
    font-weight: 400;
    letter-spacing: 2px;
  }
  .product-label__type {
    display: block;
    font-size: 20px;
    font-weight: 300;
    letter-spacing: 1px;
  }
</style>
</head>
<body>
  <main class="print-area">
    <h1 class="brand-vertical">VELQUETE</h1>
    <p class="product-label">
      <span class="product-label__name">VELQUETE</span>
      <span class="product-label__type">remover cream</span>
    </p>
  </main>
</body>
</html>
```